Open Horizon Table - invitation / brochure

​​I am in need of a bi-fold invitation/brochure for an educational series called "Open Horizon Table". This dinner series provides education and community for "Women in Transition" these are women who are currently getting divorced, recently divorced, or widowed.

I am a partner of a wealth management boutique that advises a small number of high-net-worth families. Additionally, I am married to one of the most prominent family law attorneys in the country. The combination of these two unique perspectives has allowed me to see there is an unfortunate dearth of impactful, powerful, and useful resources to help wealthy women transition from being married to being single. (via divorce and/or death of their spouse)

What, How & WHY I do my job:
As a wealth manager, the "what" and "how" aspects of my job are not materially different from most of my competitors. However, the thing that makes me completely unique, and without competition, is "why" I do my job.

I do this because so many women experience unwelcome and unproductive feelings when the dilution of their marriage is complete AND because there is virtually no good place for them to obtain the important information they truly need to move forward and lead a happy, full, prosperous, productive, and fun life. In the absence of this information, many women experience unwelcome, unpleasant, and unproductive emotions.

For example, some experience shame or fear that they have failed. Others struggle with the belief they wasted a significant portion of their life. Some struggle with unresolved anger over the entire experience. It's very difficult to process and work through these emotions by yourself and it can be hard to get the support and guidance they need from their best friends (most are not trained in this area) may well be married (functional or otherwise) and they often times don't have the times to be there when the newly divorced or widowed women need them most.

Usually, these negative feelings are most intense when they are looking backward in time. However, I have seen women go on and lead remarkably impressive lives. Lives that are ​more ​full, richer, more fun, dynamic, and rewarding than they expected possible.

More about the WHY I do what I do - I created Open Horizon Table so women in transition have a safe, supportive and comfortable space for these women to support each other. While each woman's story is unique, the emotional consequences are fairly common and they do not need to feel alone as they process the sometimes difficult, conflicting, and unpredictable emotions.

I want them to connect with each other because they have a great appreciation and empathy for what all the other women are experiencing. A bi-product of attending and participating in the dinner is to forge friendships and connections with the other woman in attendance so they can be resources to each other when they need help dealing with their own fear, anxiety, or anger. IMPORTANT NOTE - THIS IS NOT A THERAPY OR SUPPORT GROUP. Instead, this is a select group of very successful and accomplished women who have a shared experience and while each is navigating their own path, they have an opportunity to learn important information, in a safe place, where they can share their experience, strength, and hope with each other.

I want the invitation/brochure to feel very bespoke, thoughtfully curated, and specifically designed to address the most important and impactful areas of life, health, and wellness. I want the invitation/brochure to communicate that the presenters are the best in class and thought leaders in their respective areas of expertise. I also want to communicate that they have so much to be excited about. Because they have substantial financial resources, they have a unique opportunity to reinvent themselves and lead a life beyond their wildest dreams. I hope they can see how and why they can stop feeling the negative feelings of anger, sadness, fear, guilt, remorse, and regret. My goal is to get them to look forward (as opposed to backward where the negative emotions come from) so they can be optimistic, excited, happy, joyful, and enthusiastic because they get to be whoever they want; live wherever and however they want. They are not defined nor controlled by their past. They have full control and abundant resources at their disposal to be happier and more fulfilled than they ever hoped or imagined.

The feelings of optimism, excitement, energetic, and joyfulness are very important to the messaging of the Open Horizon Table. I'd like this to be a consistent theme throughout the invitation/brochure. Basically moving from a dark, sad, and negative past to a bright, fun, optimistic, rewarding, fulfilling, and dynamic future.

To create an exciting, rewarding and vibrant life they will want to (in some cases need to) learn new information and skills from the leading authorities in the most important and impactful areas of life.

The presenters at each dinner will focus on one of the "8 Dimensions of Wellness" so they can make thoughtful and informed decisions without fear, anxiety, and stress.

If you think of marriage as two people sailing a ship or flying a plane, the husband and wife often divide the responsibilities of running their affairs because it's too much for one person to manage all by themselves; besides they have a spouse who can help and often times they have different expertise. For illustration purposes, let's say the husband manages the even-numbered items and the wife manages the odd number of items. Each manages half but together everything is well managed and nothing falls through the cracks.

Post-divorce, the husband and wife now each have their own boat to sail and are responsible for all the items (odd and even-numbered) of their ship.

Unfortunately, these women are having to manage items that she has little to no experience with the even-numbered items the husband used to manage during the marriage. They have to take sole control of complicated matters that have serious and long-lasting consequences. That's great if they do a good job. However, given the scope, scale, and complexity of 7-10 figure net worth chances are they won't have the experience, expertise, intellectual resources, and time to manage all the even and odd numbers optimally.

The format of the Open Horizon Table events will be an intimate dinner conversation, in a private room, at a 5 star restaurant in Chicago. There will be a thoughtfully curated group of 4-10 women at one round table to facilitate an interesting and informative presentation. It will be specifically curated for them and delivered. There is no cost to attend the event and they are welcome to attend as many as they like. I will be covering all the expenses related to dinner, drinks, valet parking, and the speaker or presenter.

Each monthly dinner will focus on 1 of the 8 Dimensions of Wellness:

1. Physical - Physical Activity, Good Nutrition, Sleep, Preventing Illness & Injury, and Managing Chronic Health Conditions.

2. Emotional - Coping Effectively with life and creating satisfying relationships.

3. Social - Developing a sense of connection, belonging, and a well-developed support system.

4. Intellectual - Recognizing one’s creative abilities and finding ways to expand knowledge and skills. Boost cognitive function, stimulate the brain, and fuel learning.

5. Environmental - Occupying pleasant, stimulating environments that support well-being.

6. Spiritual - Expanding a sense of purpose and meaning in life, including one’s morals and ethics. (May or may not involve religious activities). Meditation

7. Vocational - Gaining personal satisfaction and enrichment from one's work (maybe academic or professional). Share your talents, wisdom, and experience.

8. Financial - Satisfaction with current and future financial situations.

I'd like the invitation/brochure to give a general overview of the 8 dimensions of wellness and that each gathering will focus on one of the eight. The presentation will be done by women (some of whom went through a divorce or the death of a spouse) who are widely recognized as experts in their respective fields. The female presenters will be highly qualified and credentialed in their field - this could mean they are MDs or PhDs and/or have decades of experience in their specific area of expertise.

I'd like the invitation to be "timeless" meaning that it doesn't have specific dates, times, or locations included. However, if someone would like more information and details they can call or email me for the specific details of the next couple of dates, topics, locations, and menus. I am also open to having a QR code available on the brochure for them to contact me for additional information. Once they contact my office they will receive I will receive all the detailed information via a PDF so they can RSVP if they would like to attend. My goal is that I don't want the invitation/brochure to expire even though the event details change every month.

I will market the Open Horizon Table program by distributing the invitation/brochures available via therapists, divorce lawyers, and grief counselors that specialize in this demographic of women in transition. They in turn will share the invitation/brochure with their woman in transition clients if they think they would benefit from the program

The look and feel I am going for with the brochure/invitation is high-end, contemporary, carefully curated content for a very special and specific community of high-net-worth women in transition that has the resources to be and do anything they want.

Velmora
Silver Larches
Ottavin
PayRo Onyx Card
Shopping in Paris and London
Flying private
Vacationing in the Riviera & Monaco.
Beautiful people
Multi-generational - kids and grandkids.

The theme, feel, and messaging of the invitation/brochure should be consistent with the concept of moving away from – sadness, fear, regret, failure, and negative. And moving towards – joyful, happy, optimistic, exciting, successful, energetic, and contentment.

This information is intended to be informative, empowering, uplifting, transformational, and helpful - so they can lead a life that is bigger, brighter, and better than they ever dreamed of experiencing.

Target Market(s)

Wealthy woman who are currently getting divorced, recently divorced, or widowed. Generally the women will be mid-fourties and older..

Industry/Entity Type

Financial Services targeting wealthy windows and divorced woman.

Font styles to use
Serif
Sans Serif

Requirements
Must have
• The look and feel I am going for with the brochure/invitation is high-end, contemporary, carefully curated content for a very special and specific community of high-net-worth women in transition that has the resources to be and do anything they want. PLEASE ENSURE 70% OF THE WOMAN IN THE INVITATAION/BROCHURE OF NON-WHITE RACES & ETHNICITIES. The theme, feel, and messaging of the invitation/brochure should be consistent with the concept of moving away from – sadness, fear, regret, failure, and negative. And moving towards – joyful, happy, optimistic, exciting, successful, energetic, and contentment. This information is intended to be informative, empowering, uplifting, transformational, and helpful - so they can lead a life that is bigger, brighter, and better than they ever dreamed of experiencing.

```html
<!DOCTYPE html>
<html lang="en">
<head>
<meta charset="utf-8">
<title>Open Horizon Table – 8 Dimensions of Wellness</title>
<link href="https://fonts.googleapis.com/css2?family=Montserrat:wght@400;500;600;700&family=Playfair+Display:wght@500;700&family=Great+Vibes&display=swap" rel="stylesheet">
<style>
  :root{
    --canvas:#ffffff;
    --page-light:#fdeee8;
    --page-peach:#f8d5c8;
    --page-rose:#f3b9a6;
    --ink:#3d3340;
    --ink-soft:#5b4f58;
    --accent:#e2795f;
    --accent-deep:#c9574a;
    --dim-social:#8cc63f;
    --dim-physical:#b5d334;
    --dim-spiritual:#2bb5a4;
    --dim-emotional:#2a9fd8;
    --dim-vocational:#56c1e8;
    --dim-intellectual:#7a5cc4;
    --dim-environmental:#5a3d9a;
    --dim-financial:#2e2f6e;
  }
  *{box-sizing:border-box;margin:0;padding:0}
  html,body{width:809px;height:1200px;overflow:hidden;background:var(--canvas)}
  body{position:relative;font-family:"Montserrat",Arial,sans-serif;color:var(--ink)}

  .spread{position:absolute;left:24px;width:761px;box-shadow:0 2px 8px rgba(0,0,0,.18);overflow:hidden}
  .spread--cover{top:12px;height:536px;display:flex}
  .spread--dimensions{top:580px;height:608px;background:linear-gradient(180deg,var(--page-peach),var(--page-light) 60%,var(--page-peach))}

  /* cover spread */
  .page{position:relative;width:50%;height:100%}
  .page--intro{background:var(--page-light);padding:18px 22px}
  .page--title{background:linear-gradient(160deg,var(--page-light) 0%,var(--page-peach) 45%,var(--page-rose) 100%)}

  .intro-lead{font-size:10.5px;line-height:1.45;color:var(--ink-soft)}
  .intro-lead strong{color:var(--accent-deep);font-weight:600}
  .venue-photo{margin:16px 0 18px;width:100%;height:196px;background:linear-gradient(135deg,#e9e4df 0%,#cfc6bd 40%,#f3efe9 70%,#b9aea3 100%)}
  .intro-copy{font-size:9.6px;line-height:1.5;color:var(--ink-soft);margin-bottom:12px}

  .title-lockup{position:absolute;left:30px;top:30px;width:340px;height:170px}
  .title-eight{position:absolute;left:0;top:-14px;font-family:"Playfair Display",Georgia,serif;font-weight:700;font-size:160px;line-height:1;color:var(--accent)}
  .title-dimensions{position:absolute;left:104px;top:34px;font-family:"Playfair Display",Georgia,serif;font-weight:500;font-size:26px;letter-spacing:1px;text-transform:uppercase;color:var(--accent-deep);white-space:nowrap}
  .title-wellness{position:absolute;left:128px;top:62px;font-family:"Great Vibes",cursive;font-size:44px;line-height:1.1;color:var(--accent-deep);white-space:nowrap}
  .title-series{position:absolute;left:124px;top:130px;font-size:12px;font-weight:600;letter-spacing:1.5px;color:var(--accent-deep);white-space:nowrap}
  .women-illustration{position:absolute;left:40px;right:0;bottom:0;height:300px;background:linear-gradient(120deg,#d9503f 0%,#8e3b6e 40%,#4b2f6e 70%,#f0a48b 100%);clip-path:polygon(18% 0,100% 8%,100% 100%,0 100%,4% 40%)}

  /* dimensions spread */
  .dims-title{position:absolute;left:30px;top:20px;display:flex;align-items:flex-end;gap:8px}
  .dims-title .num{font-family:"Playfair Display",Georgia,serif;font-weight:700;font-size:56px;line-height:.9;color:var(--accent)}
  .dims-title .words{font-family:"Playfair Display",Georgia,serif;font-size:22px;line-height:1.1;color:var(--ink)}

  .dimension{position:absolute;left:0;width:761px;height:60px;color:var(--dim)}
  .dimension__lead{position:absolute;top:8px;right:363px;height:42px;display:flex;align-items:center}
  .dimension__label{font-size:13px;font-weight:600;letter-spacing:1px;white-space:nowrap;margin:0 10px}
  .dimension__icon{flex:none;width:42px;height:42px;border-radius:50%;background:#fff;border:3px solid var(--dim)}
  .dimension__link{flex:1;min-width:14px;height:2px;background:var(--dim)}
  .dimension__bar{position:absolute;left:398px;top:4px;width:363px;height:52px;background:rgba(255,255,255,.55);border-left:12px solid var(--dim);padding:6px 12px;font-size:11px;line-height:1.35;color:var(--ink);font-weight:500;overflow:hidden}

  .dimension--social{top:84px;--dim:var(--dim-social)}
  .dimension--physical{top:148px;--dim:var(--dim-physical)}
  .dimension--spiritual{top:212px;--dim:var(--dim-spiritual)}
  .dimension--emotional{top:276px;--dim:var(--dim-emotional)}
  .dimension--vocational{top:340px;--dim:var(--dim-vocational)}
  .dimension--intellectual{top:404px;--dim:var(--dim-intellectual)}
  .dimension--environmental{top:468px;--dim:var(--dim-environmental)}
  .dimension--financial{top:532px;--dim:var(--dim-financial)}
</style>
</head>
<body>

<section class="spread spread--cover">
  <div class="page page--intro">
    <p class="intro-lead">Join us in a <strong>high-end dinner</strong> in a private room at a <strong>5-star restaurant</strong> and learn to manage your life in given circumstances. <strong>Plan the next chapter of your life according to your own rules.</strong></p>
    <div class="venue-photo" role="img" aria-label="Elegantly set dinner table in a private restaurant room"></div>
    <p class="intro-copy">Connect with others who have a great appreciation for what you are experiencing.</p>
    <p class="intro-copy">Forge &amp; make new friendships &amp; connection that will allow you to be a resource to one another when you feel fear, anxiety or anger creep into your thoughts.</p>
    <p class="intro-copy">The format of the event will be informative and educational presentation between the presenter &amp; the attendees. We hope to help the attendees with a carefully curated presentation for their demographics.</p>
  </div>
  <div class="page page--title">
    <div class="title-lockup">
      <span class="title-eight">8</span>
      <span class="title-dimensions">Dimensions</span>
      <span class="title-wellness">of Wellness</span>
      <span class="title-series">OPEN HORIZON TABLE</span>
    </div>
    <div class="women-illustration" role="img" aria-label="Illustration of four women in profile looking forward"></div>
  </div>
</section>

<section class="spread spread--dimensions">
  <h1 class="dims-title"><span class="num">8</span><span class="words">Dimensions<br>of Wellness</span></h1>

  <div class="dimension dimension--social">
    <div class="dimension__lead" style="left:200px"><span class="dimension__icon"></span><span class="dimension__label">SOCIAL</span><span class="dimension__link"></span></div>
    <p class="dimension__bar">Developing a sense of connection, belonging, and a well-developed support system.</p>
  </div>
  <div class="dimension dimension--physical">
    <div class="dimension__lead" style="left:30px"><span class="dimension__label">PHYSICAL</span><span class="dimension__icon"></span><span class="dimension__link"></span></div>
    <p class="dimension__bar">Physical Activity, Good Nutrition, Sleep, Preventing Illness &amp; Manage Chronic Health Conditions.</p>
  </div>
  <div class="dimension dimension--spiritual">
    <div class="dimension__lead" style="left:200px"><span class="dimension__icon"></span><span class="dimension__label">SPIRITUAL</span><span class="dimension__link"></span></div>
    <p class="dimension__bar">Expanding a sense of purpose &amp; meaning in life, including one's morals and ethics. (May or may not involve religion)</p>
  </div>
  <div class="dimension dimension--emotional">
    <div class="dimension__lead" style="left:24px"><span class="dimension__label">EMOTIONAL</span><span class="dimension__icon"></span><span class="dimension__link"></span></div>
    <p class="dimension__bar">Coping Effectively with life and creating satisfying relationships.</p>
  </div>
  <div class="dimension dimension--vocational">
    <div class="dimension__lead" style="left:200px"><span class="dimension__icon"></span><span class="dimension__label">VOCATIONAL</span><span class="dimension__link"></span></div>
    <p class="dimension__bar">Gaining personal satisfaction and enrichment from one's work.</p>
  </div>
  <div class="dimension dimension--intellectual">
    <div class="dimension__lead" style="left:10px"><span class="dimension__label">INTELLECTUAL</span><span class="dimension__icon"></span><span class="dimension__link"></span></div>
    <p class="dimension__bar">Recognizing one's creative abilities and finding ways to expand knowledge and skills. Boost cognitive function.</p>
  </div>
  <div class="dimension dimension--environmental">
    <div class="dimension__lead" style="left:200px"><span class="dimension__icon"></span><span class="dimension__label">ENVIRONMENTAL</span><span class="dimension__link"></span></div>
    <p class="dimension__bar">Occupying pleasant, stimulating environments that support well-being.</p>
  </div>
  <div class="dimension dimension--financial">
    <div class="dimension__lead" style="left:30px"><span class="dimension__label">FINANCIAL</span><span class="dimension__icon"></span><span class="dimension__link"></span></div>
    <p class="dimension__bar">Satisfaction with current and future financial situations.</p>
  </div>
</section>

</body>
</html>
```